Looking for label design for pet health products (antimicrobial spray)

We are a start up company based in Singapore. We are manufacturing and selling antimicrobial spray for pets. Our product brand name is OrchidaVane. The spray is mainly useful for cuts, sores, bacterial and fungal skin infections, wounds, dermatitis.The antimicrobial spray contains colloidal silver with Neem herbal extract. This product is free from synthetic chemicals, it is safe for internal and external use.

The target customers are pet owners. The means of sales would be e-commerce websites as well as retail stores. Primary market is Singapore and Asia. Label should be attractive to pet owners.

The label size of 15 cm in length and 7 cm in height is expected. The label is to be placed on amber colored plastic bottles of around 250 ml volume. The maximum number of colors should be three.

It Company

```html
<!DOCTYPE html>
<html lang="en">
<head>
<meta charset="utf-8">
<title>OrchidaVane – Antimicrobial for pets label</title>
<link href="https://fonts.googleapis.com/css2?family=Open+Sans:wght@400;600;700&display=swap" rel="stylesheet">
<style>
  :root {
    --page: #ffffff;
    --label-blue: #b8e4f8;
    --ink: #0e5c8a;
    --rule: #1a6690;
    --panel: #ffffff;
  }
  * { margin: 0; padding: 0; box-sizing: border-box; }
  html, body {
    width: 1200px; height: 1000px; overflow: hidden;
    background: var(--page);
    font-family: "Open Sans", sans-serif;
    color: var(--ink);
  }
  .label {
    position: absolute; left: 22px; top: 305px;
    width: 1156px; height: 390px;
    background: var(--label-blue);
  }
  .grid-lines { position: absolute; left: 0; top: 0; }
  .info-box {
    position: absolute; background: var(--panel);
    padding: 4px 8px; line-height: 1.3;
  }
  .info-box .heading { font-size: 19px; }
  .info-box .body { font-size: 18px; }
  .ingredients { left: 24px; top: 27px; width: 300px; height: 106px; }
  .uses { left: 826px; top: 27px; width: 285px; height: 106px; }
  .claim {
    position: absolute; left: 24px; width: 296px; height: 36px;
    background: var(--panel); font-size: 17px;
    padding: 6px 10px; white-space: nowrap;
  }
  .claim.storage { top: 246px; }
  .claim.natural { top: 289px; }
  .claim.safety { top: 333px; }
  .mascot {
    position: absolute; left: 437px; top: 30px;
    width: 236px; height: 200px; border-radius: 50%;
    background: radial-gradient(ellipse at center, #ffffff 55%, #eef7fc 100%);
  }
  .brand {
    position: absolute; left: 380px; top: 238px; width: 350px;
    text-align: center;
  }
  .brand-name { font-size: 46px; font-weight: 700; letter-spacing: -1px; line-height: 1.1; }
  .tagline {
    font-size: 21px; letter-spacing: 0.5px; margin-top: 4px;
    border-top: 2px solid var(--rule); display: inline-block; padding-top: 2px;
  }
  .net-volume {
    position: absolute; left: 380px; top: 356px; width: 350px;
    text-align: center; font-size: 11px;
  }
  .website { position: absolute; left: 848px; top: 256px; font-size: 18px; letter-spacing: 0.5px; }
  .origin { position: absolute; left: 848px; top: 342px; font-size: 18px; letter-spacing: 0.5px; }
</style>
</head>
<body>
  <section class="label">
    <svg class="grid-lines" width="1156" height="390" viewBox="0 0 1156 390" aria-hidden="true">
      <g stroke="var(--rule)" stroke-width="4" fill="none">
        <line x1="324" y1="65" x2="395" y2="65"/>
        <line x1="385" y1="0" x2="385" y2="130"/>
        <line x1="412" y1="0" x2="412" y2="135"/>
        <line x1="438" y1="0" x2="438" y2="125"/>
        <line x1="372" y1="22" x2="462" y2="22"/>
        <line x1="372" y1="110" x2="440" y2="110"/>
        <line x1="690" y1="22" x2="780" y2="22"/>
        <line x1="705" y1="0" x2="705" y2="125"/>
        <line x1="732" y1="0" x2="732" y2="135"/>
        <line x1="758" y1="0" x2="758" y2="130"/>
        <line x1="758" y1="65" x2="826" y2="65"/>
      </g>
    </svg>

    <div class="info-box ingredients">
      <p class="heading">Contains:-</p>
      <p class="body">Deionized water,Colloidal Silver, Neem extract.</p>
    </div>

    <div class="info-box uses">
      <p class="heading">Useful for:-</p>
      <p class="body">Cuts,Dermatitis,Bacterial and Fungal infections, Sores,Wounds.</p>
    </div>

    <div class="mascot" role="img" aria-label="Cartoon illustration of a white puppy with blue ears and a red collar, sitting"></div>

    <div class="brand">
      <p class="brand-name">OrchidaVane</p>
      <p class="tagline">Antimicrobial for pets</p>
    </div>
    <p class="net-volume">Net Vol : 250mL,20ppm</p>

    <p class="claim storage">Store in cool &amp; dark place.</p>
    <p class="claim natural">Free from synthetic chemicals.</p>
    <p class="claim safety">Safe for Internal &amp; External use.</p>

    <p class="website">www.orchidavane.com</p>
    <p class="origin">Product of Singapore</p>
  </section>
</body>
</html>
```